Modern Design Business Card industrial maintenance company

Business card design for Company named Brookvale Equipment Services

Target Market(s)

Industrial

Industry/Entity Type

Maintenance and repair

Contact Information for Business Card

Place holder for address, office phone, mobile number and email

Requirements
Must have
• Clean modern look
Nice to have
• N/a

```html
<!DOCTYPE html>
<html lang="en">
<head>
<meta charset="utf-8">
<title>Brookvale Equipment Services — Business Card</title>
<link href="https://fonts.googleapis.com/css2?family=Poppins:wght@400;500;600&display=swap" rel="stylesheet">
<style>
  :root {
    --stage: #2e2e2e;
    --ink: #111111;
    --paper: #ffffff;
    --text: #1a1a1a;
    --muted: #3a3a3a;
    --rule: #b5b5b5;
    --gloss-1: #1b1b1b;
    --gloss-2: #2c2c2c;
  }
  * { box-sizing: border-box; margin: 0; padding: 0; }
  html, body { width: 1200px; height: 689px; overflow: hidden; }
  body {
    background: var(--stage);
    font-family: "Poppins", sans-serif;
    position: relative;
  }
  .card {
    position: absolute;
    top: 196px;
    width: 520px;
    height: 297px;
    border-radius: 18px;
    overflow: hidden;
  }
  /* Back face */
  .card--back { left: 50px; background: var(--ink); }
  .card-back__pattern {
    position: absolute; inset: 0;
    background: radial-gradient(ellipse at 70% 20%, var(--gloss-2), var(--gloss-1) 70%);
  }
  .card-back__brand {
    position: absolute;
    left: 0; right: 0; top: 118px;
    text-align: center;
    color: var(--paper);
    font-weight: 600;
    line-height: 1.1;
  }
  .brand-name { font-size: 30px; letter-spacing: 2px; }
  .brand-tag { font-size: 10px; letter-spacing: 4px; }

  /* Front face */
  .card--front { left: 630px; background: var(--paper); }
  .card-front__brand {
    position: absolute;
    left: 26px; top: 84px; width: 220px;
    text-align: center;
    color: var(--ink);
    font-weight: 600;
    line-height: 1.15;
  }
  .brand-mark {
    width: 54px; height: 54px;
    border: 3px solid var(--ink);
    border-radius: 50%;
    margin: 0 auto 10px;
  }
  .card-front__brand .brand-name { font-size: 26px; letter-spacing: 1.5px; }
  .card-front__brand .brand-tag { font-size: 8.5px; letter-spacing: 3px; }

  .divider {
    position: absolute;
    left: 262px; top: 40px;
    width: 1px; height: 170px;
    background: linear-gradient(var(--paper), var(--rule) 40%, var(--paper));
  }
  .contact {
    position: absolute;
    left: 284px; top: 44px;
    color: var(--text);
  }
  .contact__name { font-size: 17px; font-weight: 600; letter-spacing: 0.5px; }
  .contact__role { font-size: 12px; color: var(--muted); margin-bottom: 12px; }
  .contact__row {
    display: flex; align-items: center; gap: 7px;
    font-size: 12.5px; line-height: 1.55;
  }
  .contact__row svg { width: 11px; height: 11px; fill: var(--ink); flex: none; }
  .contact__address { font-size: 12.5px; line-height: 1.4; margin-top: 10px; }

  .band {
    position: absolute; left: 0; right: 0; bottom: 0;
    height: 42px; background: var(--ink);
  }
  .band-rule {
    position: absolute; left: 0; right: 0; bottom: 48px;
    height: 2px; background: var(--ink);
  }
  .band-seal {
    position: absolute; right: 26px; bottom: 20px;
    width: 44px; height: 44px; border-radius: 50%;
    background: var(--paper); border: 3px solid var(--ink);
  }
</style>
</head>
<body>
  <section class="card card--back" aria-label="Card back">
    <div class="card-back__pattern" role="img" aria-label="Repeating gloss brand-mark pattern on matte black"></div>
    <div class="card-back__brand">
      <div class="brand-name">BROOKVALE</div>
      <div class="brand-tag">EQUIPMENT SERVICES</div>
    </div>
  </section>

  <section class="card card--front" aria-label="Card front">
    <div class="card-front__brand">
      <div class="brand-mark"></div>
      <div class="brand-name">BROOKVALE</div>
      <div class="brand-tag">EQUIPMENT SERVICES</div>
    </div>

    <div class="divider"></div>

    <div class="contact">
      <div class="contact__name">MARCUS HALE</div>
      <div class="contact__role">Managing Director</div>
      <div class="contact__row">
        <svg viewBox="0 0 24 24" aria-hidden="true"><path d="M6.6 10.8a15.1 15.1 0 0 0 6.6 6.6l2.2-2.2a1 1 0 0 1 1-.25 11.4 11.4 0 0 0 3.6.57 1 1 0 0 1 1 1V20a1 1 0 0 1-1 1A17 17 0 0 1 3 4a1 1 0 0 1 1-1h3.5a1 1 0 0 1 1 1c0 1.25.2 2.45.57 3.57a1 1 0 0 1-.25 1z"/></svg>
        <span>044-987 654 321</span>
      </div>
      <div class="contact__row">
        <svg viewBox="0 0 24 24" aria-hidden="true"><path d="M2 5h20v14H2z M2 5l10 8 10-8" fill="none" stroke="#111" stroke-width="2"/><path d="M2 5h20l-10 8z"/></svg>
        <span>info@brookvale-es.com</span>
      </div>
      <div class="contact__row">
        <svg viewBox="0 0 24 24" aria-hidden="true"><circle cx="12" cy="12" r="10"/><path d="M2 12h20M12 2c3 3 3 17 0 20M12 2c-3 3-3 17 0 20" stroke="#fff" stroke-width="1.4" fill="none"/></svg>
        <span>www.brookvale-es.com</span>
      </div>
      <div class="contact__address">188, Foundry Lane Works<br>30917, Eastmoor Region</div>
    </div>

    <div class="band-rule"></div>
    <div class="band"></div>
    <div class="band-seal"></div>
  </section>
</body>
</html>
```